Rise As Captain Book Cover Design

Book Cover Design Brief
Book Title
Rise As Captain
Subtitle
The 10 Quiet Habits of Remarkable Command
Author
Orwen Dalquist
Overview
This book is about leadership that starts within.
Most leadership books focus on tactics or management strategies. This book focuses on the inner disciplines that create powerful leaders — mindset, integrity, focus, empathy, professionalism, honesty, and self-respect.
The tone of the book is bold, direct, confident, and transformational.
This is not a soft or corporate leadership book. It is a call to step up and become the leader you are capable of becoming.
The cover should feel:
• Powerful
• Professional
• Transformational
• Premium
• Memorable
Think best-selling leadership book, not a generic business book.
Target Audience
Business owners
Managers
Entrepreneurs
Team leaders
Professionals who want to grow as leaders
Most readers are ambitious professionals who want to level up their leadership and life.
Design Direction
The design should communicate:
Strength. Discipline. Leadership. Personal transformation.
Avoid cliché leadership visuals like:
• Handshakes
• Office buildings
• Corporate stock imagery
• Teams sitting around tables
The design should feel iconic, bold, and timeless.
Think about covers of successful leadership books such as:
Copper Rituals
Total Stewardship
Won't Break Now
Begin From Purpose
The 36 Rules of Sway
These covers are simple, powerful, and recognizable even at small sizes.
Typography
The title RISE AS CAPTAIN should be:
• Bold
• Strong
• Dominant on the cover
• Easy to read even at small sizes (important for Vellora thumbnails)
The subtitle should be clean and secondary to the title.
The overall typography should feel strong, modern, and premium.
Color Direction
Designers are free to explore colors, but the cover should feel strong and premium, not playful.
Colors that often work well for leadership books include:
Black
Gold
White
Deep blue
Dark red
High contrast and clarity are important.
Style
Preferred style:
• Clean
• Modern
• Minimal
• Strong contrast
Avoid clutter and overly busy designs.
The goal is to create a cover that feels powerful and professional at first glance.
Deliverables
Front cover design for a leadership book.
Final files should include:
• High resolution artwork
• Editable source files
• Print-ready version suitable for publishing
Goal of the Cover
When someone sees this book on Vellora or in a bookstore, they should immediately think:
“This looks like a serious leadership book.”
The design should feel like it belongs next to books by authors such as:
Marcus Thorley
Brandt Osgood
Peter Hollis
Nolan Fairbrook
A strong, confident cover that attracts leaders who want to grow and perform at a higher level.
Target Market(s)
Business Owners and High level managers
Look and feel
Each slider illustrates characteristics of the customer's brand and the style your logo design should communicate.

```html
<!DOCTYPE html>
<html lang="en">
<head>
<meta charset="utf-8">
<title>Rise As Captain — Cover Wrap</title>
<link rel="stylesheet" href="https://fonts.googleapis.com/css2?family=Bebas+Neue&family=Tinos:ital@0;1&display=swap">
<style>
  :root {
    --page-bg: #f2f2f2;
    --cover-top: #2b2b2b;
    --cover-bottom: #050505;
    --spine-bg: #141414;
    --gold: #c8962e;
    --white: #ffffff;
    --body-text: #d9d9d9;
    --bulb-glow: #3a2f18;
    --bulb-dim: #1c1c1c;
  }
  * { box-sizing: border-box; margin: 0; padding: 0; }
  html, body { width: 817px; height: 1200px; overflow: hidden; background: var(--page-bg); }
  .canvas { position: relative; width: 817px; height: 1200px; }

  .wrap {
    position: absolute; left: 20px; top: 331px; width: 777px; height: 538px;
    background: linear-gradient(180deg, var(--cover-top) 0%, #151515 55%, var(--cover-bottom) 100%);
    box-shadow: 0 2px 6px rgba(0,0,0,.35);
    overflow: hidden;
    font-family: "Bebas Neue", "Arial Narrow", sans-serif;
  }
  .panel { position: absolute; top: 0; height: 100%; }
  .back { left: 0; width: 359px; }
  .spine { left: 359px; width: 59px; background: linear-gradient(180deg, #1d1d1d, #0a0a0a); }
  .front { left: 418px; width: 359px; }

  .kicker {
    position: absolute; writing-mode: vertical-rl; color: var(--white);
    line-height: 1; letter-spacing: 1px; white-space: nowrap;
  }
  .title {
    position: absolute; color: var(--gold); line-height: .8; white-space: nowrap; letter-spacing: 1px;
  }
  .subtitle { position: absolute; color: var(--gold); line-height: 1.1; white-space: nowrap; text-align: center; }

  /* back */
  .back .kicker { left: 88px; top: 47px; font-size: 22px; }
  .back .title { left: 110px; top: 44px; font-size: 74px; }
  .back .subtitle { left: 0; width: 359px; top: 108px; font-size: 16px; }
  .blurb {
    position: absolute; left: 26px; top: 148px; width: 307px;
    font-family: "Tinos", "Times New Roman", serif; font-size: 8.6px; line-height: 11px;
    color: var(--body-text); text-align: justify;
  }
  .blurb p + p { margin-top: 11px; }
  .author-photo { position: absolute; left: 26px; top: 364px; width: 89px; height: 118px; background: var(--white); }
  .about {
    position: absolute; left: 134px; top: 354px; width: 197px;
    font-family: "Tinos", "Times New Roman", serif; color: var(--body-text);
  }
  .about h2 { font-style: italic; font-weight: 400; font-size: 12px; letter-spacing: .5px; margin-bottom: 8px; color: var(--white); }
  .about p { font-size: 7.6px; line-height: 10px; text-align: justify; }
  .about p + p { margin-top: 10px; }

  /* spine */
  .spine-mark {
    position: absolute; left: 4px; top: 10px; width: 52px; height: 42px;
    background: radial-gradient(circle at 85% 40%, var(--bulb-glow), transparent 45%),
                radial-gradient(ellipse at 40% 50%, #2a2a2a, transparent 70%);
  }
  .spine-title {
    position: absolute; left: 7px; top: 198px; writing-mode: vertical-rl;
    line-height: 1; white-space: nowrap; display: flex; align-items: flex-start;
  }
  .spine-title .kicker-sm { color: var(--white); font-size: 17px; position: static; margin-bottom: 4px; }
  .spine-title .title-sm { color: var(--gold); font-size: 50px; line-height: .8; }
  .spine-author {
    position: absolute; left: 8px; top: 456px; writing-mode: vertical-rl;
    color: var(--white); font-size: 20px; line-height: .95; white-space: nowrap;
  }

  /* front */
  .front .kicker { left: 60px; top: 52px; font-size: 32px; }
  .front .title { left: 91px; top: 46px; font-size: 102px; }
  .front .subtitle { left: 0; width: 359px; top: 134px; font-size: 21px; }
  .bulbs {
    position: absolute; left: 82px; top: 206px; width: 202px; height: 264px;
    background:
      radial-gradient(ellipse 22% 22% at 50% 18%, var(--bulb-glow), transparent 100%),
      radial-gradient(ellipse 60% 55% at 50% 65%, var(--bulb-dim), transparent 100%);
  }
  .front-author {
    position: absolute; left: 0; width: 359px; top: 506px; text-align: center;
    color: var(--white); font-size: 21px; letter-spacing: .5px;
  }
</style>
</head>
<body>
<div class="canvas">
  <div class="wrap">
    <section class="panel back">
      <span class="kicker">RISE AS</span>
      <h1 class="title">CAPTAIN</h1>
      <p class="subtitle">THE 10 QUIET HABITS OF REMARKABLE COMMAND</p>
      <div class="blurb">
        <p>Lorem ipsum dolor sit amet, consectetuer adipiscing elit, sed diam nonummy nibh euismod tincidunt ut laoreet dolore magna aliquam erat volutpat. Ut wisi enim ad minim veniam, quis nostrud exerci tation ullamcorper suscipit lobortis nisl ut aliquip ex ea commodo consequat.</p>
        <p>Duis autem vel eum iriure dolor in hendrerit in vulputate velit esse molestie consequat, vel illum dolore eu feugiat nulla facilisis at vero eros et accumsan et iusto odio dignissim qui blandit praesent luptatum zzril delenit augue duis dolore te feugait nulla facilisi.</p>
        <p>Lorem ipsum dolor sit amet, cons ectetuer adipiscing elit, sed diam nonummy nibh euismod tincidunt ut laoreet dolore magna aliquam erat volutpat. Ut wisi enim ad minim veniam, quis nostrud exerci tation ullamcorper suscipit lobortis nisl ut aliquip ex ea commodo consequat.</p>
        <p>Lorem ipsum dolor sit amet, consectetuer adipiscing elit, sed diam nonummy nibh euismod tincidunt ut laoreet</p>
      </div>
      <div class="author-photo" role="img" aria-label="Author portrait"></div>
      <div class="about">
        <h2>ABOUT AUTHOR</h2>
        <p>Duis autem vel eum iriure dolor in hendrerit in vulputate velit esse molestie consequat, vel illum dolore eu feugiat nulla facilisis at vero eros et accumsan et iusto odio dignissim qui blandit praesent luptatum zzril delenit augue duis dolore te feugait nulla facilisi.</p>
        <p>Lorem ipsum dolor sit amet, cons ectetuer adipiscing elit, sed diam nonummy nibh euismod tincidunt ut laoreet dolore magna aliquam erat volutpat. Ut wisi enim ad minim veniam, quis nostrud exerci tation ullamcorper suscipit lobortis nisl ut aliquip ex ea commodo consequat.</p>
      </div>
    </section>

    <section class="panel spine">
      <div class="spine-mark" role="img" aria-label="Small cluster of light bulbs with one glowing gold"></div>
      <div class="spine-title">
        <span class="kicker-sm">RISE AS</span>
        <span class="title-sm">CAPTAIN</span>
      </div>
      <div class="spine-author">ORWEN<br>DALQUIST</div>
    </section>

    <section class="panel front">
      <span class="kicker">RISE AS</span>
      <h1 class="title">CAPTAIN</h1>
      <p class="subtitle">THE 10 QUIET HABITS OF<br>REMARKABLE COMMAND</p>
      <div class="bulbs" role="img" aria-label="Pyramid of outlined light bulbs, the top one glowing gold and the rest fading into the dark"></div>
      <p class="front-author">ORWEN DALQUIST</p>
    </section>
  </div>
</div>
</body>
</html>
```